Interdisciplinary research group seeking illustration

We are an interdisciplinary research group based in Denmark, with a focus on musculoskeletal health in youth. Our goal is to improve health and function of adolescents, by generating knowledge and evidence that will lead to better understanding, treatment and prevention of adolescent musculoskeletal pain. We are looking to design an image that can be used on our webpage, in news reports, and grant applications that represents our research strategy.

Our vision is to have the image represent the two important concepts in our research:
1. Understanding and preventing musculoskeletal pain in youth
2. Stratifying and optimising managing of those with pain
The image should represent that these factors are interacting and interdependent.
We have uploaded some sketches with important keywords and concepts, but would like an illustration which can represent these ideas visually (e.g. rather than the words 'environment' or 'pain' etc., these should be images). These are only suggestions and designers can feel free to adapt them to their own creative ideas and designs. We don't have any preference but are looking for something that can be understood by both the general public and researchers.
The focus should be on kids/ youth, and perhaps include children passing from the beginning with no pain, to developing pain, and recovering and returning to the start. The colour red and green can be used to represent the positive and negative outcomes.

Target Market(s)

Both the general population and researchers

Industry/Entity Type

Health

Requirements
Must have
• Children/ youth as part of the image

```html
<!DOCTYPE html>
<html lang="en">
<head>
<meta charset="utf-8">
<title>Research strategy: youth musculoskeletal pain</title>
<link rel="stylesheet" href="https://fonts.googleapis.com/css2?family=Barlow:ital,wght@0,600;0,700;1,500;1,700;1,800&display=swap">
<style>
  :root {
    --orange: #f26b22;
    --orange-soft: #f5893f;
    --orange-light: #f7a062;
    --sky: #6ccde3;
    --red: #e8262a;
    --green: #25a244;
    --white: #ffffff;
  }
  html, body { margin: 0; padding: 0; overflow: hidden; background: var(--white); }
  .canvas {
    position: relative; width: 1200px; height: 1200px; overflow: hidden;
    background: var(--white); font-family: "Barlow", "Helvetica Neue", Arial, sans-serif;
  }
  .abs { position: absolute; margin: 0; white-space: nowrap; }
  .pillar-title { font-weight: 700; font-size: 34px; line-height: 1; top: 196px; width: 478px; text-align: center; }
  .pillar-title.understand { left: 106px; color: var(--orange); }
  .pillar-title.manage { left: 616px; color: var(--sky); }
  .pillar-box { top: 240px; height: 119px; width: 478px; }
  .pillar-box.understand { left: 106px; background: var(--orange); }
  .pillar-box.manage { left: 616px; background: var(--sky); }
  .pillar-text { color: var(--white); font-style: italic; font-weight: 500; font-size: 24px; line-height: 25px; }
  .factor { color: var(--orange-soft); font-weight: 700; font-size: 34px; line-height: 1; left: 224px; }
  .factor-note { color: var(--orange-soft); font-style: italic; font-weight: 500; font-size: 23px; line-height: 1; left: 224px; top: 483px; }
  .child-figure { background: linear-gradient(180deg, var(--orange-light), var(--orange)); border-radius: 10px; }
  .influence { color: var(--red); font-style: italic; font-weight: 500; font-size: 24px; line-height: 1; }
  .pain-word { color: var(--red); font-style: italic; font-weight: 800; line-height: 1; }
  .outcome { font-style: italic; font-weight: 800; font-size: 31px; line-height: 1; }
  .outcome.recovery { color: var(--green); left: 946px; top: 550px; }
  .outcome.persistence { color: var(--red); left: 904px; top: 753px; }
  .mood { border-radius: 50%; width: 44px; height: 44px; box-sizing: border-box; }
  .mood.good { left: 1051px; top: 502px; border: 3px solid var(--green); background: #e6f5ea; }
  .mood.bad { left: 1051px; top: 706px; border: 3px solid var(--red); background: #fde8e8; }
</style>
</head>
<body>
<div class="canvas">

  <h2 class="abs pillar-title understand">Understand &amp; Prevent</h2>
  <h2 class="abs pillar-title manage">Stratify &amp; Manage</h2>

  <div class="abs pillar-box understand"></div>
  <div class="abs pillar-box manage"></div>

  <svg class="abs" style="left:116px;top:252px" width="80" height="98" viewBox="0 0 80 98" aria-label="Lightbulb icon" role="img">
    <g fill="none" stroke="#fff" stroke-width="5" stroke-linecap="round">
      <line x1="40" y1="2" x2="40" y2="14"/>
      <line x1="14" y1="10" x2="21" y2="20"/>
      <line x1="66" y1="10" x2="59" y2="20"/>
      <line x1="2" y1="30" x2="13" y2="34"/>
      <line x1="78" y1="30" x2="67" y2="34"/>
    </g>
    <path d="M40 22 a20 20 0 0 1 12 36 v10 h-24 v-10 a20 20 0 0 1 12 -36z" fill="#fff"/>
    <rect x="28" y="72" width="24" height="5" rx="2" fill="#fff"/>
    <rect x="28" y="80" width="24" height="5" rx="2" fill="#fff"/>
    <rect x="32" y="88" width="16" height="5" rx="2" fill="#fff"/>
  </svg>
  <p class="abs pillar-text" style="left:224px;top:266px">Understand risk of pain to inform<br>treatment and prevention</p>

  <svg class="abs" style="left:630px;top:252px" width="94" height="94" viewBox="0 0 88 88" aria-label="Gear icon with a kid at its centre" role="img">
    <g fill="#fff">
      <rect x="38" y="0" width="12" height="16" rx="2"/>
      <rect x="38" y="72" width="12" height="16" rx="2"/>
      <rect x="0" y="38" width="16" height="12" rx="2"/>
      <rect x="72" y="38" width="16" height="12" rx="2"/>
      <rect x="38" y="0" width="12" height="16" rx="2" transform="rotate(45 44 44)"/>
      <rect x="38" y="72" width="12" height="16" rx="2" transform="rotate(45 44 44)"/>
      <rect x="0" y="38" width="16" height="12" rx="2" transform="rotate(45 44 44)"/>
      <rect x="72" y="38" width="16" height="12" rx="2" transform="rotate(45 44 44)"/>
      <circle cx="44" cy="44" r="32"/>
    </g>
    <circle cx="44" cy="44" r="22" fill="var(--sky)"/>
    <circle cx="44" cy="44" r="14" fill="#fff"/>
  </svg>
  <p class="abs pillar-text" style="left:736px;top:264px">Simple 1st line treatments<br>empowering self-management in<br>kids and their surroundings</p>

  <div class="abs child-figure" role="img" aria-label="Icon: two parents with their child" style="left:120px;top:402px;width:74px;height:48px;border-radius:30px 30px 6px 6px"></div>
  <div class="abs child-figure" role="img" aria-label="Icon: a child running, for sports" style="left:120px;top:480px;width:74px;height:74px"></div>
  <div class="abs child-figure" role="img" aria-label="Icon: a young head in profile showing the brain" style="left:120px;top:619px;width:74px;height:87px;border-radius:37px 37px 8px 8px"></div>
  <div class="abs child-figure" role="img" aria-label="Icon: a child standing with raised arms" style="left:120px;top:768px;width:74px;height:108px"></div>

  <h3 class="abs factor" style="top:447px">Enviorement</h3>
  <p class="abs factor-note">(parents &amp; sports)</p>
  <h3 class="abs factor" style="top:644px">Psychology</h3>
  <h3 class="abs factor" style="top:803px">Physiology</h3>

  <svg class="abs" style="left:0;top:0" width="1200" height="1200" viewBox="0 0 1200 1200" aria-hidden="true">
    <g stroke="var(--red)" stroke-width="4" stroke-linecap="round" fill="none">
      <line x1="774" y1="606" x2="688" y2="494"/>
      <line x1="786" y1="606" x2="802" y2="440"/>
      <line x1="798" y1="606" x2="888" y2="508"/>
    </g>
    <line x1="456" y1="664" x2="912" y2="664" stroke="var(--red)" stroke-width="6"/>
    <path d="M444 664 l24 -17 v34z" fill="var(--red)"/>
    <path d="M924 664 l-24 -17 v34z" fill="var(--red)"/>
    <g stroke-width="9" stroke-linecap="square" fill="none">
      <line x1="916" y1="644" x2="956" y2="606" stroke="var(--green)"/>
      <line x1="916" y1="686" x2="956" y2="724" stroke="var(--red)"/>
    </g>
    <path d="M970 594 l-6 28 l-22 -22z" fill="var(--green)"/>
    <path d="M970 738 l-28 -6 l22 -22z" fill="var(--red)"/>
  </svg>

  <p class="abs influence" style="left:638px;top:452px">Diagnosis</p>
  <p class="abs influence" style="left:756px;top:397px">Parents?!</p>
  <p class="abs influence" style="left:860px;top:452px">care-behavior</p>

  <p class="abs pain-word" style="left:514px;top:610px;font-size:50px">PAIN</p>
  <p class="abs pain-word" style="left:674px;top:619px;font-size:40px">experience</p>

  <div class="abs mood good" role="img" aria-label="Happy face symbol"></div>
  <p class="abs outcome recovery">RECOVERY</p>
  <div class="abs mood bad" role="img" aria-label="Sad face symbol"></div>
  <p class="abs outcome persistence">PERSISTENCE</p>

</div>
</body>
</html>
```